Contemporary Media Company with Logo Needs Business Card Design

Need a modern card design for a full service digital media company using the logo included. Also want the info below on the card. Probably list the services on the card back to save space for the front. Want something contemporary to impress prospective clients. You may want to submit both a somewhat more conservative design, and then a more wild one.
General Info: (this phrase need not be on the card)
Tod Parvin
Founder and CEO
949-628-4513
tod@lumavantstudio.example
lumavantstudio.example
Services: (this word need not be on the card)
Content & Experience Strategy
Brand Development
Search Engine Optimization
Website Design
Website Operation
Social Media Integration
Complete Video Solutions
Industry/Entity Type
Business
Contact Information for Business Card
Tod Parvin
Founder and CEO
949-628-4513
tod@lumavantstudio.example
lumavantstudio.example
Brand Development
Website Design
Website Operation
Social Media Integration
Complete Video Solutions
Look and feel

```html
<!DOCTYPE html>
<html lang="en">
<head>
<meta charset="utf-8">
<title>Lumavant Studio – Business Cards</title>
<link href="https://fonts.googleapis.com/css2?family=Open+Sans:wght@400;600;700&display=swap" rel="stylesheet">
<style>
  :root {
    --bg: #ecebe8;
    --white: #ffffff;
    --black: #0d0d0d;
    --ink: #4a4a4a;
    --grey: #6e6e6e;
    --orange: #f0821e;
    --line: #8a8a8a;
  }
  * { margin: 0; padding: 0; box-sizing: border-box; }
  html, body { width: 1200px; height: 913px; overflow: hidden; }
  body {
    background: var(--bg);
    font-family: "Open Sans", Arial, sans-serif;
    position: relative;
  }
  .card {
    position: absolute;
    top: 302px;
    width: 540px;
    height: 309px;
    overflow: hidden;
    box-shadow: 0 6px 18px rgba(0,0,0,.18);
  }
  .card--front { left: 40px; background: var(--white); }
  .card--back { left: 620px; background: var(--black); }

  .brand {
    position: absolute;
    display: flex;
    align-items: center;
    gap: 14px;
  }
  .brand__square { width: 34px; height: 34px; background: var(--orange); }
  .brand__name {
    font-weight: 600;
    font-size: 30px;
    letter-spacing: 3px;
    line-height: 1;
    text-transform: uppercase;
  }
  .card--front .brand { left: 40px; top: 72px; }
  .card--front .brand__name { color: var(--grey); }
  .card--back .brand { left: 120px; top: 62px; }
  .card--back .brand__name { color: var(--white); }

  .divider {
    position: absolute;
    left: 0; right: 0;
    top: 178px;
    height: 1px;
    background: var(--line);
  }
  .person { position: absolute; left: 30px; top: 130px; }
  .person__name { font-weight: 700; font-size: 20px; color: var(--ink); line-height: 1.1; }
  .person__title { font-weight: 600; font-size: 14px; color: var(--orange); }

  .contact {
    position: absolute;
    right: 22px;
    top: 112px;
    list-style: none;
    text-align: right;
    font-size: 12px;
    color: var(--ink);
    line-height: 17px;
  }
  .contact li { display: flex; justify-content: flex-end; align-items: center; gap: 6px; }
  .contact svg { width: 11px; height: 11px; }

  .band { position: absolute; }
  .card--front .band--orange { left: 300px; right: 0; top: 178px; height: 22px; background: var(--orange); }
  .card--front .band--grey { left: 0; width: 300px; top: 222px; height: 34px; background: var(--grey); }
  .band-mark { position: absolute; width: 14px; height: 14px; background: var(--orange); }
  .card--front .band-mark { left: 280px; top: 196px; }

  .card--back .band--orange { left: 330px; right: 0; top: 140px; height: 24px; background: var(--orange); }
  .card--back .band--white { left: 0; width: 330px; top: 250px; height: 22px; background: var(--white); }
  .card--back .band-mark { left: 310px; top: 160px; }

  .services {
    position: absolute;
    left: 40px;
    top: 150px;
    list-style: none;
    color: var(--white);
    font-size: 12.5px;
    line-height: 13.5px;
  }
  .services li { display: flex; align-items: center; gap: 7px; }
  .services li::before {
    content: "";
    width: 5px; height: 5px;
    background: var(--orange);
  }
</style>
</head>
<body>

<section class="card card--front" aria-label="Card front">
  <div class="brand">
    <span class="brand__square"></span>
    <span class="brand__name">Lumavant Studio</span>
  </div>

  <div class="person">
    <p class="person__name">Tod Parvin</p>
    <p class="person__title">Founder and CEO</p>
  </div>

  <ul class="contact">
    <li>949-628-4513
      <svg viewBox="0 0 12 12"><path d="M3 1 L5 3.5 L4 5 Q5 7 7 8 L8.5 7 L11 9 L9.5 11 Q4 10.5 1 2.5 Z" fill="#f0821e"/></svg>
    </li>
    <li>tod@lumavantstudio.example
      <svg viewBox="0 0 12 12"><rect x="1" y="2.5" width="10" height="7" fill="none" stroke="#f0821e" stroke-width="1.3"/><path d="M1 2.5 L6 6.5 L11 2.5" fill="none" stroke="#f0821e" stroke-width="1.3"/></svg>
    </li>
    <li>www.lumavantstudio.example
      <svg viewBox="0 0 12 12"><circle cx="6" cy="6" r="5" fill="none" stroke="#f0821e" stroke-width="1.2"/><path d="M1 6 H11 M6 1 Q3 6 6 11 M6 1 Q9 6 6 11" fill="none" stroke="#f0821e" stroke-width="1"/></svg>
    </li>
  </ul>

  <div class="divider"></div>
  <div class="band band--orange"></div>
  <div class="band band--grey"></div>
  <span class="band-mark"></span>
</section>

<section class="card card--back" aria-label="Card back">
  <div class="brand">
    <span class="brand__square"></span>
    <span class="brand__name">Lumavant Studio</span>
  </div>

  <ul class="services">
    <li>Content &amp; Experience Strategy</li>
    <li>Brand Development</li>
    <li>Search Engine Optimization</li>
    <li>Website Design</li>
    <li>Website Operation</li>
    <li>Social Media Integration</li>
    <li>Complete Video Solutions</li>
  </ul>

  <div class="band band--orange"></div>
  <div class="band band--white"></div>
  <span class="band-mark"></span>
</section>

</body>
</html>
```